Pet Spa Brochure

We are currently rebranding our Pet Resort & Spa. We have already completed our new website (www.tlmanimalhaven.com), business cards and logo (attached). We are currently working on our brochures and decided to take a different route in finishing them.

We are looking for a spa/massage, floral, oriental, relaxing, feminine and elegant design for the brochure specific to our Pet Spa services. We want professional and elegant but also original and unique if possible.

We mainly have dog customers but we also have cat customers so a picture of at least one cat would be perfect. Our Pet Resort (not Spa, just Resort) brochure can be found at www.tlmanimalhaven.com/rates and is the first two links listed. If things work well for our Pet Spa brochure we will be going back to redo the Pet Resort brochure as well.

I'm uploading a psd of the current brochure design so that you have access to the content. I can adjust the files later to make everything (or anything new) fit but please take the amount of text (present and future) into account when doing the design. I'm also uploading the psd of our current logo so it can be incorporated into the brochure as well.

The final design should communicate elegance, relaxation, pampering and happiness.
Updates

I'm attaching some of our pictures with pets in our pool, as well as some photos I saw on pixaroundly that show dogs being pampered/rubbed/massaged. The links to the photos are below. I'll be uploading the others to the project attachment area.

Target Market(s)

Women between the ages of 25 and 55

Industry/Entity Type

Business

Requirements
Must have
• Animals, paw prints, our logo, floral, oriental hot springs/spa feel.
Should not have
• Cartoon animals or cartoon like clipart.

```html
<!DOCTYPE html>
<html lang="en">
<head>
<meta charset="utf-8">
<title>TLM Pet Haven &amp; Spa – Spa Services</title>
<link rel="stylesheet" href="https://fonts.googleapis.com/css2?family=Amaranth&family=Lobster&display=swap">
<style>
  :root {
    --ink: #2f2a2c;
    --magenta: #c2185f;
    --crimson: #b5135a;
    --frame-grey: #5a5a5a;
    --blush: #f6e6f0;
    --lilac: #ead7ea;
    --swirl: rgba(214, 170, 210, 0.35);
    --logo-orange: #e0662a;
  }
  * { box-sizing: border-box; margin: 0; padding: 0; }
  html, body { width: 1200px; height: 926px; overflow: hidden; background: #fff; }
  .brochure {
    position: relative;
    width: 1200px;
    height: 926px;
    overflow: hidden;
    font-family: "Amaranth", sans-serif;
    font-size: 13px;
    color: var(--ink);
    background:
      radial-gradient(ellipse 700px 420px at 1100px 880px, var(--lilac), transparent 70%),
      radial-gradient(ellipse 600px 300px at 200px 420px, var(--blush), transparent 70%),
      linear-gradient(180deg, #fff 0%, #fdf8fb 50%, #f6ebf3 100%);
  }
  .swirls { position: absolute; inset: 0; }
  .heading {
    position: absolute;
    font-family: "Lobster", cursive;
    font-weight: 400;
    font-size: 25px;
    color: var(--magenta);
    text-align: center;
    width: 320px;
  }
  .heading--feline { left: 38px; top: 281px; }
  .heading--canine { left: 442px; top: 50px; }
  .heading--extras { left: 843px; top: 50px; }

  .menu { position: absolute; line-height: 22px; }
  .menu--feline { left: 38px; top: 335px; width: 318px; }
  .menu--canine { left: 445px; top: 104px; width: 309px; }
  .menu--extras { left: 842px; top: 103px; width: 308px; }
  .item + .item { margin-top: 22px; }
  .row { display: flex; align-items: baseline; white-space: nowrap; }
  .dots {
    flex: 1;
    margin: 0 3px;
    border-bottom: 1.5px dotted var(--ink);
    transform: translateY(-3px);
  }
  .tier { display: flex; }
  .tier .weight { width: 133px; }
  .footnote { position: absolute; left: 445px; top: 852px; line-height: 22px; }

  .brand {
    position: absolute;
    left: 96px; top: 60px;
    width: 210px;
    display: flex; flex-direction: column; align-items: center; gap: 14px;
  }
  .brand .mark { width: 96px; height: 96px; border-radius: 50%; background: var(--logo-orange); }
  .brand .name { font-size: 22px; color: var(--crimson); text-align: center; line-height: 26px; }

  .photo { position: absolute; border-radius: 50%; }
  .photo--cat {
    left: 188px; top: 548px; width: 184px; height: 184px;
    border: 5px solid var(--frame-grey);
    background: radial-gradient(circle at 45% 45%, #a89a86, #6b5e4d 70%, #4a3f33);
  }
  .photo--dog {
    left: 24px; top: 657px; width: 226px; height: 226px;
    border: 5px solid var(--crimson);
    background: radial-gradient(circle at 50% 50%, #f3efe9, #d9d0c6 60%, #9fa6c6);
  }
</style>
</head>
<body>
<main class="brochure">
  <svg class="swirls" width="1200" height="926" aria-hidden="true">
    <path d="M0 330 C 250 250, 420 430, 640 360 S 950 200, 1200 330" fill="none" stroke="var(--swirl)" stroke-width="30"/>
    <path d="M0 420 C 300 330, 520 620, 760 520 S 1050 380, 1200 460" fill="none" stroke="var(--swirl)" stroke-width="18"/>
    <path d="M380 926 C 520 700, 700 560, 1200 600" fill="none" stroke="var(--swirl)" stroke-width="40"/>
    <path d="M500 926 C 640 760, 860 660, 1200 700" fill="none" stroke="var(--swirl)" stroke-width="14"/>
  </svg>

  <div class="brand">
    <span class="mark"></span>
    <span class="name">TLM Pet Haven &amp; Spa</span>
  </div>

  <h2 class="heading heading--feline">Feline Spa Services</h2>
  <section class="menu menu--feline">
    <div class="item row"><span>Bath</span><span class="dots"></span><span>$25</span></div>
    <div class="item row"><span>Bath &amp; Nails</span><span class="dots"></span><span>$30</span></div>
    <div class="item row"><span>Flea Bath</span><span class="dots"></span><span>$30</span></div>
    <div class="item row"><span>Nails Only</span><span class="dots"></span><span>$10</span></div>
    <div class="item row"><span>Brushout/Dematting</span><span class="dots"></span><span>$40/hr + Bath</span></div>
  </section>

  <div class="photo photo--cat" role="img" aria-label="Photo of a tabby cat nuzzling its owner"></div>
  <div class="photo photo--dog" role="img" aria-label="Photo of a small white terrier in a bathtub"></div>

  <h2 class="heading heading--canine">Canine Spa Services</h2>
  <section class="menu menu--canine">
    <div class="item">
      <div class="row"><span>Bath</span><span class="dots"></span><span>See Below</span></div>
      <div class="tier"><span class="weight">Under 20 lbs</span><span>$20</span></div>
      <div class="tier"><span class="weight">81–110 lbs</span><span>$35</span></div>
      <div class="tier"><span class="weight">21–50 lbs</span><span>$25</span></div>
      <div class="tier"><span class="weight">51–80 lbs</span><span>$30</span></div>
      <div class="tier"><span class="weight">111 lbs &amp; Over</span><span>$40</span></div>
    </div>
    <div class="item">
      <div class="row"><span>Bath &amp; Nails</span><span class="dots"></span><span>See Below</span></div>
      <div class="tier"><span class="weight">Under 20 lbs</span><span>$25</span></div>
      <div class="tier"><span class="weight">81–110 lbs</span><span>$40</span></div>
      <div class="tier"><span class="weight">21–50 lbs</span><span>$30</span></div>
      <div class="tier"><span class="weight">51–80 lbs</span><span>$35</span></div>
      <div class="tier"><span class="weight">111 lbs &amp; Over</span><span>$45</span></div>
    </div>
    <div class="item row"><span>Nails Only</span><span class="dots"></span><span>$10</span></div>
    <div class="item row"><span>Brushout/Dematting</span><span class="dots"></span><span>$40/hr + Bath</span></div>
    <div class="item">
      <div class="row"><span>Professional Grooming<sup>*</sup></span><span class="dots"></span><span>See Below</span></div>
      <div class="tier"><span class="weight">Under 20lbs</span><span>At Least $40</span></div>
      <div class="tier"><span class="weight">21–50 lbs</span><span>At Least $50</span></div>
      <div class="tier"><span class="weight">51–80 lbs</span><span>At Least $60</span></div>
      <div class="tier"><span class="weight">81–110 lbs</span><span>At Least $70</span></div>
      <div class="tier"><span class="weight">111 lbs &amp; Over</span><span>At Least $80</span></div>
    </div>
    <div class="item row"><span>Shedless Program*</span><span class="dots"></span><span>$60 to $115</span></div>
    <div class="item row"><span>Flea Bath</span><span class="dots"></span><span>$3 to $10 + Bath</span></div>
    <div class="item row"><span>Special Bath</span><span class="dots"></span><span>$3 to $10 + Bath</span></div>
    <div class="item row"><span>Long Coats</span><span class="dots"></span><span>Extra Charge</span></div>
  </section>
  <p class="footnote">*Includes the price of a Bath in the rate.</p>

  <h2 class="heading heading--extras">Canine Spa Extras</h2>
  <section class="menu menu--extras">
    <div class="item row"><span>Anal Glands</span><span class="dots"></span><span>$??</span></div>
    <div class="item row"><span>Scent of the Month</span><span class="dots"></span><span>$5 + Bath</span></div>
    <div class="item row"><span>Bows/Bandannas</span><span class="dots"></span><span>$??</span></div>
    <div class="item row"><span>Creative Grooming</span><span class="dots"></span><span>$??</span></div>
    <div class="item row"><span>Whitening Treatment</span><span class="dots"></span><span>$??</span></div>
    <div class="item row"><span>Teeth Brushing</span><span class="dots"></span><span>$??</span></div>
    <div class="item">
      <div class="row"><span>Temporary Airbrush Tattoos</span><span class="dots"></span><span>See Below</span></div>
      <div class="tier"><span class="weight">Under 20lbs</span><span>At Least $40</span></div>
      <div class="tier"><span class="weight">21–50 lbs</span><span>At Least $50</span></div>
      <div class="tier"><span class="weight">51–80 lbs</span><span>At Least $60</span></div>
      <div class="tier"><span class="weight">81–110 lbs</span><span>At Least $70</span></div>
      <div class="tier"><span class="weight">111 lbs &amp; Over</span><span>At Least $80</span></div>
    </div>
    <div class="item row"><span>Nail Polish</span><span class="dots"></span><span>$60 to $115</span></div>
    <div class="item row"><span>Hot Towel Massage</span><span class="dots"></span><span>$10</span></div>
    <div class="item row"><span>Hot Spring Session</span><span class="dots"></span><span>$20</span></div>
    <div class="item row"><span>Hot Spring &amp; Towel Massage</span><span class="dots"></span><span>$25</span></div>
    <div class="item row"><span>Playtime</span><span class="dots"></span><span>$7</span></div>
    <div class="item row"><span>Downtime</span><span class="dots"></span><span>$10</span></div>
  </section>
</main>
</body>
</html>
```